Business Card Design

Business card design and logo for new company called PRT Holdings, Inc.
No specific business product line so design would be more focused on the Company name and type style. I would like logo to incorporate Company Lettering "PRT" . Classic example of that would be the Vex Broadcasting logo. Intent that the "PRT" lettering design would also be the Company Logo design.
Note that contact information for business card does not have telephone / fax numbers and web site as that will follow but make allowance for that information in the business card design. Several of the design layouts has small logo instead of the wording for phone, fax ..... which I would prefer.
Target Market(s)
Small Businesses
Industry/Entity Type
Business
Contact Information for Business Card
Dennis Lamb
PRT Holdings, Inc.
48216 Fernhill Lane, Unit B
Larkmoor, NV 93512
Phone: 555.218.6403
Mobile: 555.731.2954
FAX: 555.731.8162
Email: dlamb@prtholdings.example
Web: www.prtholdings.example
Font styles to use
Other font styles liked:
- Helvetica
Look and feel

```html
<!DOCTYPE html>
<html lang="en">
<head>
<meta charset="utf-8">
<title>PRT Holdings, Inc. — Business Card</title>
<link rel="stylesheet" href="https://fonts.googleapis.com/css2?family=Open+Sans:wght@400;600;700&display=swap">
<style>
  :root {
    --backdrop: #2b2b2b;
    --card-black: #1c1c1c;
    --brand-red: #a3151f;
    --paper-white: #ffffff;
    --text-white: #f4f4f4;
  }
  * { margin: 0; padding: 0; box-sizing: border-box; }
  html, body {
    width: 1200px;
    height: 1000px;
    overflow: hidden;
    background: var(--backdrop);
    font-family: "Open Sans", Helvetica, Arial, sans-serif;
  }
  .canvas {
    position: relative;
    width: 1200px;
    height: 1000px;
    display: flex;
    align-items: center;
    justify-content: center;
  }
  .business-card {
    position: relative;
    width: 900px;
    height: 514px;
    background: var(--card-black);
    color: var(--text-white);
    box-shadow: 0 24px 50px rgba(0, 0, 0, 0.55);
    overflow: hidden;
  }
  .brand {
    position: absolute;
    top: 130px;
    left: 0;
    right: 0;
    display: flex;
    align-items: center;
    justify-content: center;
    gap: 18px;
  }
  .brand-square {
    width: 40px;
    height: 40px;
    background: var(--brand-red);
  }
  .brand-name {
    font-weight: 600;
    font-size: 52px;
    letter-spacing: 2px;
    color: var(--text-white);
    line-height: 1;
    white-space: nowrap;
  }
  .contact {
    position: absolute;
    top: 292px;
    left: 0;
    right: 0;
    text-align: center;
  }
  .contact-name {
    font-weight: 600;
    font-size: 30px;
    letter-spacing: 2.5px;
    text-transform: uppercase;
    margin-bottom: 12px;
  }
  .contact-address {
    font-weight: 400;
    font-size: 22px;
    letter-spacing: 1.2px;
    white-space: nowrap;
  }
  .stripe-band {
    position: absolute;
    left: 0;
    bottom: 0;
    width: 100%;
    height: 24px;
    display: block;
  }
</style>
</head>
<body>
  <main class="canvas">
    <article class="business-card">
      <div class="brand">
        <span class="brand-square" aria-hidden="true"></span>
        <span class="brand-name">PRT Holdings, Inc.</span>
      </div>

      <div class="contact">
        <p class="contact-name">Dennis Lamb</p>
        <p class="contact-address">48216 Fernhill Lane, Unit B Larkmoor, NV 93512</p>
      </div>

      <svg class="stripe-band" viewBox="0 0 900 24" preserveAspectRatio="none" aria-hidden="true">
        <rect x="0" y="0" width="900" height="24" fill="var(--brand-red)"/>
        <rect x="120" y="0" width="125" height="24" fill="var(--paper-white)"/>
        <rect x="375" y="0" width="125" height="24" fill="var(--paper-white)"/>
        <rect x="630" y="0" width="125" height="24" fill="var(--paper-white)"/>
      </svg>
    </article>
  </main>
</body>
</html>
```